Vesprine Oakville Cabernet Sauvignon-Wine label design

We need a package design for an up market wine brand named, Vesprine. It will be a Cabernet Sauvignon from the Oakville AVA of Napa Valley. We are looking for a stylish modern label that will stand out on a retail shelf. We want the label to be attention grabbing and stylish while presenting an up market luxury brand.

Sick

Requirements
Must have
• Must have the words(in order of importance)
-Vesprine
-Cabernet Sauvignon
-Oakville
-Napa Valley
-2018

Must be designed for a traditional "Bordeaux" style bottle (Bottle specs in uploaded files)
Should not have
• Any images of grapes, vineyards, wine glasses or bottles

```html
<!DOCTYPE html>
<html lang="en">
<head>
<meta charset="UTF-8">
<title>Vesprine Oakville Cabernet Sauvignon – Label</title>
<link href="https://fonts.googleapis.com/css2?family=Playfair+Display:wght@400&family=Montserrat:wght@500&display=swap" rel="stylesheet">
<style>
  :root {
    --backdrop: #e6e6e4;
    --label-white: #ffffff;
    --ink: #1a1a1a;
    --band: #231f20;
    --band-text: #f4f4f4;
  }
  * { margin: 0; padding: 0; box-sizing: border-box; }
  html, body {
    width: 1200px;
    height: 900px;
    overflow: hidden;
    background: var(--backdrop);
  }
  .label {
    position: absolute;
    left: 345px;
    top: 60px;
    width: 510px;
    height: 780px;
    background: var(--label-white);
    box-shadow: 0 6px 24px rgba(0,0,0,0.12);
    color: var(--ink);
    text-align: center;
  }
  .brand-name {
    position: absolute;
    top: 218px;
    left: 0;
    right: 0;
    font-family: "Playfair Display", serif;
    font-weight: 400;
    font-size: 72px;
    line-height: 1;
    color: var(--ink);
  }
  .varietal {
    position: absolute;
    top: 418px;
    left: 0;
    right: 0;
    font-family: "Playfair Display", serif;
    font-size: 28px;
    line-height: 1.35;
    letter-spacing: 0.22em;
    padding-left: 0.22em;
  }
  .appellation {
    position: absolute;
    top: 590px;
    left: 0;
    right: 0;
    font-family: "Montserrat", sans-serif;
    font-weight: 500;
  }
  .appellation .ava {
    font-size: 15px;
    letter-spacing: 0.3em;
    padding-left: 0.3em;
  }
  .appellation .region {
    margin-top: 6px;
    font-size: 9px;
    letter-spacing: 1.5em;
    padding-left: 1.5em;
  }
  .vintage-band {
    position: absolute;
    top: 666px;
    left: 0;
    right: 0;
    height: 60px;
    background: var(--band);
    color: var(--band-text);
    font-family: "Playfair Display", serif;
    font-size: 21px;
    line-height: 60px;
    letter-spacing: 0.05em;
  }
</style>
</head>
<body>
  <main class="label">
    <h1 class="brand-name">Vesprine</h1>
    <p class="varietal">CABERNET<br>SAUVIGNON</p>
    <div class="appellation">
      <p class="ava">OAKVILLE</p>
      <p class="region">NAPA VALLEY</p>
    </div>
    <div class="vintage-band">2018</div>
  </main>
</body>
</html>
```